Business Card Design Project - Brantwell Media

We need a new business card that fits with our new logo. We are a social media agency and consultancy operating in China. We want a fresh and strong business card. Our cards need to be two-sided as we have both English and Chinese language names and addresses on the card, but as with our current business card this does not need to be a mirror-image. Our thoughts go out to a white card on the front where the logo/name is and then using the logo colours for different coloured back-grounds. i.e that the back of the biz card works with the four different colours in the logo.

Attached is the new logo, and also a copy of our old business cards.

Target Market(s)

CEO's, CMO's. media and advertising professionals

Industry/Entity Type

Business

Requirements
Must have
• inclusion of both Chinese and English language
Nice to have
• four different colored versions of the back of the biz card. Our logo has four colors and each of these colors we would like to have a version of.

```html
<!DOCTYPE html>
<html lang="en">
<head>
<meta charset="utf-8">
<title>Brantwell Media – Business Cards</title>
<link rel="stylesheet" href="https://fonts.googleapis.com/css2?family=Arimo:wght@700&family=Open+Sans:wght@400;600&family=Noto+Serif+SC:wght@400&display=swap">
<style>
  :root {
    --backdrop: #2b2b2b;
    --card-white: #f4f4f4;
    --brand-green: #7dc52a;
    --ink: #111111;
    --ink-soft: #555555;
    --on-green: #ffffff;
    --logo-light: #eef2e6;
    --logo-faint: rgba(255, 255, 255, 0.28);
  }
  * { margin: 0; padding: 0; box-sizing: border-box; }
  html, body { width: 1200px; height: 900px; overflow: hidden; }
  body {
    background: var(--backdrop);
    font-family: "Open Sans", Arial, sans-serif;
    position: relative;
  }
  .card {
    position: absolute;
    background: var(--brand-green);
    color: var(--on-green);
  }
  .card--front { left: 48px; top: 65px; width: 544px; height: 326px; background: var(--card-white); color: var(--ink); }
  .card--back-a { left: 628px; top: 65px; width: 541px; height: 323px; }
  .card--back-b { left: 48px; top: 488px; width: 542px; height: 323px; }
  .card--back-c { left: 630px; top: 487px; width: 543px; height: 324px; }

  .tab { position: absolute; top: 61px; width: 26px; height: 48px; background: var(--brand-green); }
  .tab--left { left: 0; }
  .tab--right { right: 0; }

  .front-contact {
    position: absolute; top: 79px; left: 0; right: 0;
    text-align: center; font-size: 15px; letter-spacing: 0.3px; color: var(--ink-soft);
  }
  .holder { position: absolute; left: 88px; top: 193px; }
  .holder-name { font-family: "Arimo", Arial, sans-serif; font-weight: 700; font-size: 21px; letter-spacing: 0.5px; }
  .holder-role { font-size: 13.5px; margin-left: 29px; margin-top: 2px; }

  .wordmark {
    position: absolute; font-family: "Open Sans", Arial, sans-serif; font-weight: 600;
    line-height: 1; white-space: nowrap; display: flex; align-items: center; gap: 8px;
  }
  .wordmark-dot { width: 9px; height: 9px; background: currentColor; display: inline-block; }
  .wordmark--front { left: 284px; top: 194px; font-size: 27px; color: var(--ink); }
  .wordmark--light { right: 26px; top: 40px; font-size: 40px; color: var(--logo-light); }
  .wordmark--faint { right: 36px; top: 48px; font-size: 40px; color: var(--logo-faint); }

  .address { position: absolute; font-size: 14.5px; line-height: 22px; letter-spacing: 0.2px; }
  .address-cn { font-family: "Noto Serif SC", serif; font-size: 11.5px; line-height: 17px; letter-spacing: 1px; margin-bottom: 6px; }
  .address-phone { margin-top: 12px; }
  .card--back-a .address { left: 120px; top: 182px; }
  .card--back-b .address { left: 0; right: 0; top: 93px; text-align: center; }
  .card--back-c .address { left: 22px; top: 180px; }
</style>
</head>
<body>
  <section class="card card--front" aria-label="Card front">
    <span class="tab tab--left"></span>
    <span class="tab tab--right"></span>
    <p class="front-contact">owen@hartley.com | www.brantwellchina.com</p>
    <div class="holder">
      <p class="holder-name">Owen Hartley</p>
      <p class="holder-role">managing director</p>
    </div>
    <p class="wordmark wordmark--front">Brantwell Media<span class="wordmark-dot"></span></p>
  </section>

  <section class="card card--back-a" aria-label="Card back with logo">
    <p class="wordmark wordmark--light">Brantwell Media</p>
    <div class="address">
      <p class="address-cn">北京市朝阳区东湖南路<br>岚溪商务中心二层南侧办公区B305（100020）</p>
      <p>Suite B305, Lanxi Commercial Centre</p>
      <p>Donghu South Rd Chaoyang District, Beijing 100020</p>
      <p class="address-phone">Phone: +86 13900482615 | chat: owenbeijing</p>
    </div>
  </section>

  <section class="card card--back-b" aria-label="Card back, text only">
    <div class="address">
      <p class="address-cn">北京市朝阳区东湖南路<br>岚溪商务中心二层南侧办公区B305（100020）</p>
      <p>Suite B305, Lanxi Commercial Centre</p>
      <p>Donghu South Rd Chaoyang District, Beijing 100020</p>
      <p class="address-phone">Phone: +86 13900482615 | chat: owenbeijing</p>
    </div>
  </section>

  <section class="card card--back-c" aria-label="Card back with faint logo">
    <p class="wordmark wordmark--faint">Brantwell Media</p>
    <div class="address">
      <p class="address-cn">北京市朝阳区东湖南路<br>岚溪商务中心二层南侧办公区B305（100020）</p>
      <p>Suite B305, Lanxi Commercial Centre</p>
      <p>Donghu South Rd Chaoyang District, Beijing 100020</p>
      <p class="address-phone">Phone: +86 13900482615 | chat: owenbeijing</p>
    </div>
  </section>
</body>
</html>
```